Great Opportunity !! Masters in Business Analytics College Course

the size is Full Page, with bleed*
8”x 10.75" plus 0.25" bleed.
please leave one inch for footer
the purpose is attract students to join this college program .
this is for students in USA .
college age of around 24 years old
I am looking for a flyer that is unique and shows creativity .
A flyer that people would want to look at it because it is unique.
you can choose either vector, text ,or picture.
if you do picture it should be a white USA citizen wearing a white solid shirt and not long hair

Target Market(s)

USA students about 23 in age to join this college program

Industry/Entity Type

education

Colors
0054AA
0677BA
7BADD7
CADEEF
E8F1F8
0094D4
00A9DD
6FCCEA
C7EBF8
E9F6FB

Requirements
Must have
• the text should not be crowded .. .. .. the ad should not be full of text
Should not have
• not have very large text .. it should not be a flyer that is full of text .. you have to figure out how to avoid looking at the ad and it is very busy with text

```html
<!DOCTYPE html>
<html lang="en">
<head>
<meta charset="utf-8">
<title>Harlow State College – Master's in Business Analytics</title>
<link rel="stylesheet" href="https://fonts.googleapis.com/css2?family=Oswald:wght@400;500;600&family=Roboto:ital,wght@0,400;0,700;1,700&display=swap">
<style>
  :root {
    --backdrop: #d2d2d2;
    --paper: #ffffff;
    --ink-dark: #1f2a32;
    --orange: #f28a2b;
    --teal: #20b3a3;
    --sky: #12a8dd;
    --tag-warm: #fde3cf;
    --tag-cool: #cbe9f7;
    --text: #222222;
  }
  * { box-sizing: border-box; margin: 0; padding: 0; }
  html, body { width: 1119px; height: 1200px; overflow: hidden; }
  body { background: var(--backdrop); font-family: "Roboto", Arial, sans-serif; position: relative; }

  .flyer {
    position: absolute; left: 210px; top: 125px;
    width: 708px; height: 943px;
    background: var(--paper); overflow: hidden;
  }
  .flyer-shapes { position: absolute; inset: 0; }
  .abs { position: absolute; }
  .display { font-family: "Oswald", "Arial Narrow", sans-serif; }

  .headline {
    left: 0; width: 708px; top: 170px; text-align: center;
    color: #fff; font-size: 35px; line-height: 47px; font-weight: 400;
    letter-spacing: -0.8px; text-transform: uppercase;
  }
  .headline .accent { color: var(--orange); }
  .subhead {
    left: 0; width: 708px; top: 276px; text-align: center;
    color: var(--orange); font-size: 26px; line-height: 38px; font-weight: 400;
    letter-spacing: -0.3px;
  }
  .salary {
    left: 0; width: 708px; top: 370px; text-align: center;
    color: #fff; font-size: 21px; font-weight: 400; letter-spacing: -0.3px;
  }
  .source {
    left: 0; width: 708px; top: 409px; text-align: center;
    color: #fff; font-size: 11px; font-style: italic; font-weight: 700;
  }
  .college-name {
    left: 43px; top: 473px; width: 265px; height: 59px;
    background: var(--teal); color: #fff; border-radius: 4px;
    font-size: 30px; line-height: 59px; text-align: center; letter-spacing: -0.3px;
    box-shadow: 0 10px 12px -8px rgba(0,0,0,.35);
  }
  .quote { left: 47px; top: 547px; font-size: 15px; line-height: 19px; color: var(--text); }

  .role-tag {
    position: absolute; height: 21px; padding: 0 8px; line-height: 19px;
    font-family: "Oswald", sans-serif; font-size: 12.5px; color: #222;
    border: 1px solid #8a8a8a; border-radius: 2px;
  }
  .role-tag.warm { background: var(--tag-warm); }
  .role-tag.cool { background: var(--tag-cool); }

  .hired-title { left: 45px; top: 674px; font-size: 14.5px; color: var(--text); font-weight: 500; }
  .employer {
    position: absolute; font-family: "Oswald", sans-serif; font-size: 12px; color: #222;
    display: flex; align-items: center; gap: 6px; white-space: nowrap;
  }
  .employer::before {
    content: ""; width: 10px; height: 10px; border: 1.5px solid var(--sky); display: inline-block;
  }

  .open-house-title { left: 42px; top: 770px; color: #fff; font-size: 27px; font-weight: 400; }
  .open-house-info { left: 42px; top: 811px; color: #fff; font-size: 15px; line-height: 19.5px; }

  .duration-note {
    left: 590px; width: 92px; top: 498px; text-align: center;
    font-size: 10.5px; line-height: 11.5px; color: #222;
  }
  .duration-number { left: 590px; width: 90px; top: 403px; text-align: center; color: var(--ink-dark); font-size: 46px; font-weight: 600; line-height: 50px; }
  .duration-unit { left: 590px; width: 90px; top: 456px; text-align: center; color: var(--ink-dark); font-size: 11px; }

  .analytics-illustration {
    left: 290px; top: 480px; width: 370px; height: 380px;
    background: radial-gradient(ellipse at 55% 50%, #f6a04a 0%, #9fd6cf 45%, rgba(255,255,255,0) 70%);
    border-radius: 50%;
  }
</style>
</head>
<body>
<main class="flyer">
  <svg class="flyer-shapes" width="708" height="943" viewBox="0 0 708 943" aria-hidden="true">
    <path d="M0,0 H130 C60,30 12,100 0,190 Z" fill="var(--orange)"/>
    <path d="M0,212 C25,92 110,18 205,0 H708 V300 C700,420 640,492 540,495 H0 Z" fill="var(--ink-dark)"/>
    <rect x="0" y="495" width="470" height="5" fill="var(--orange)"/>
    <path d="M192,100 Q355,40 518,100 L512,132 Q355,72 200,132 Z" fill="var(--sky)"/>
    <path d="M192,100 L200,132 L185,122 Z M518,100 L512,132 L527,122 Z" fill="#0b7fae"/>
    <path id="ribbon-arc" d="M215,120 Q355,62 500,120" fill="none"/>
    <text font-family="Oswald, sans-serif" font-size="23" font-weight="500" fill="#fff" text-anchor="middle">
      <textPath href="#ribbon-arc" startOffset="50%">JOIN THIS COLLEGE PROGRAM</textPath>
    </text>
    <g fill="#fff">
      <polygon points="322,126 325,134 333,134 327,139 329,147 322,142 315,147 317,139 311,134 319,134"/>
      <polygon points="354,115 358,126 370,126 360,133 364,145 354,138 344,145 348,133 338,126 350,126"/>
      <polygon points="386,126 389,134 397,134 391,139 393,147 386,142 379,147 381,139 375,134 383,134"/>
    </g>
    <g fill="none" stroke="#8fa3ad" stroke-width="2">
      <rect x="645" y="198" width="6" height="14"/><rect x="656" y="190" width="6" height="22"/>
      <rect x="667" y="194" width="6" height="18"/><rect x="678" y="182" width="6" height="30"/>
      <rect x="120" y="442" width="6" height="16"/><rect x="131" y="434" width="6" height="24"/>
      <rect x="142" y="438" width="6" height="20"/><rect x="153" y="428" width="6" height="30"/>
    </g>
    <polygon fill="var(--orange)" points="635,391 645,410 664,400 660,421 683,423 668,438 688,452 665,459 675,480 652,475 648,497 635,480 622,497 618,475 595,480 605,459 582,452 602,438 587,423 610,421 606,400 625,410"/>
    <path d="M0,765 H282 L400,857 H0 Z" fill="var(--sky)"/>
  </svg>

  <div class="abs headline display">Do you have <span class="accent">an analytical mind</span> and<br>seeking a profitable career?</div>
  <div class="abs subhead display">A Master's in Business Analytics – Harlow State College<br>can prepare you for some of the most in demand jobs.</div>
  <div class="abs salary display">JOBS WITH A MEDIAN SALARY OF $100K+</div>
  <div class="abs source">(National Labor Data Survey 2023)</div>

  <div class="abs duration-number display">21</div>
  <div class="abs duration-unit">MONTHS</div>
  <div class="abs duration-note">Hybrid with one weekly in-person evening meeting</div>

  <div class="abs college-name display">Harlow State College</div>
  <p class="abs quote">"Only 5% of universities achieve<br>prestigious ACBE accreditation."</p>

  <span class="role-tag warm" style="left:43px;top:607px">BI Developer</span>
  <span class="role-tag cool" style="left:139px;top:607px">Data Scientist</span>
  <span class="role-tag cool" style="left:43px;top:638px">Data Analyst</span>
  <span class="role-tag warm" style="left:139px;top:638px">Data Developer</span>

  <div class="abs hired-title display">GRADUATES WERE HIRED AT:</div>
  <span class="employer" style="left:45px;top:704px">Brenn</span>
  <span class="employer" style="left:104px;top:704px">Quorvel</span>
  <span class="employer" style="left:173px;top:704px">Vexa</span>
  <span class="employer" style="left:45px;top:727px">Skarn</span>
  <span class="employer" style="left:104px;top:727px">Halvorsen</span>

  <div class="abs open-house-title display">OPEN HOUSE</div>
  <p class="abs open-house-info">Wednesday, April 20, 7:30 pm.<br>Email alex.rivera@harlowstate.edu for the link!</p>

  <div class="abs analytics-illustration" role="img" aria-label="Isometric illustration of a laptop with growing bar charts, a rising arrow, a pie chart, a calculator and dashboard screens"></div>
</main>
</body>
</html>
```